Tomuvin 30ml pipette jar Mental Health

Label and Box for 30ml amber jar with pipette.
Already have a sample design, that needs to be adapted and possibly improved for the new packaging.
Dark brown letters on White Label.
The jar 30ml with pipette / dropper is amber with dark cap. Please view the photo.
Please view all the files, which I am uploading.
Please provide a mock up version.
Thank you.

Target Market(s)

Upscale women 34-59

Industry/Entity Type

Nutrition, Medical

Requirements
Must have
• Conservative, Minimalistic, Luxury
Should not have
• Leaves

```html
<!DOCTYPE html>
<html lang="en">
<head>
<meta charset="utf-8">
<title>Tomuvin – Label and Box</title>
<link rel="stylesheet" href="https://fonts.googleapis.com/css2?family=Barlow+Semi+Condensed:wght@500;600;700&family=Manrope:wght@300;400;600;700&display=swap">
<style>
:root{
  --page:#e2e2e2;
  --paper:#ffffff;
  --ink:#3a2f26;
  --ink-soft:#5b5149;
  --muted:#7a726b;
  --gold:#c9a86a;
  --line:#3a2f26;
}
*{box-sizing:border-box;margin:0;padding:0}
html,body{width:675px;height:1200px;overflow:hidden}
body{background:var(--page);font-family:"Manrope",sans-serif;color:var(--ink);position:relative}

.brand{display:flex;align-items:center;gap:6px;color:var(--ink);font-weight:600}
.brand-dot{width:14px;height:14px;border-radius:50%;background:var(--gold);flex:none}
.product-name{font-family:"Barlow Semi Condensed",sans-serif;font-weight:600;color:var(--ink);letter-spacing:.5px;line-height:1}
.rule{height:1.5px;background:var(--line)}
.tagline{font-size:8px;line-height:1.5;color:var(--ink-soft)}
.tagline strong{font-weight:600;color:var(--ink)}
.volume{font-size:7px;color:var(--muted);letter-spacing:.3px}
.small{font-size:5.6px;line-height:1.45;color:var(--ink-soft)}
.small b{color:var(--ink)}
.fda{border:1px solid var(--ink);padding:4px 5px;font-size:5.8px;font-weight:700;line-height:1.35}
.facts{border:1px solid var(--ink);padding:5px 6px}
.facts h3{font-family:"Barlow Semi Condensed",sans-serif;font-weight:700;font-size:13px;line-height:1.1;border-bottom:1px solid var(--ink);padding-bottom:2px;margin-bottom:3px}
.facts .row{display:flex;justify-content:space-between;font-size:5.8px;color:var(--ink-soft);line-height:1.5}
.facts .formula{border-top:3px solid var(--ink);margin-top:3px;padding-top:3px;font-size:5.8px;color:var(--ink-soft);border-bottom:1px solid var(--ink);padding-bottom:3px}
.facts .ingredients{font-size:5.8px;color:var(--ink-soft);line-height:1.45;padding-top:3px}
.base-band{position:absolute;left:0;right:0;bottom:0;height:9px;background:var(--ink)}

/* flat wrap label */
.label{position:absolute;left:20px;top:40px;width:635px;height:250px;background:var(--paper);display:grid;grid-template-columns:1fr 1fr 1fr;box-shadow:0 1px 3px rgba(0,0,0,.12)}
.label-panel{position:relative;padding:22px 16px 20px}
.label-back{display:flex;flex-direction:column;gap:10px}
.label-back .fda{margin-top:auto;margin-bottom:12px}
.label-front .brand{font-size:11px}
.label-front .product-name{font-size:34px;margin-top:40px}
.label-front .rule{margin:6px 0 18px;width:160px}
.label-front .volume{margin-top:10px}
.label-facts{display:flex;flex-direction:column;gap:10px}
.maker{font-size:5.4px;line-height:1.45;color:var(--ink-soft)}
.maker b{color:var(--ink)}
.exp{font-size:7px;font-weight:700;margin-top:auto;margin-bottom:12px}

/* flat box panels */
.box{position:absolute;left:20px;top:340px;width:635px;height:780px;display:grid;grid-template-columns:1fr 1fr 1fr;gap:20px}
.box-panel{position:relative;background:var(--paper);box-shadow:0 1px 3px rgba(0,0,0,.12);overflow:hidden}
.box-front{padding:34px 20px}
.box-front .brand{font-size:12px}
.box-front .product-name{font-size:38px;margin-top:170px}
.box-front .rule{margin:7px 0 20px}
.box-front .tagline{font-size:9px}
.box-front .volume{font-size:8px;margin-top:20px}
.box-side{display:flex;align-items:center;justify-content:center}
.side-word{transform:rotate(-90deg);white-space:nowrap;font-size:54px;color:var(--ink);letter-spacing:4px}
.side-word strong{font-weight:700}
.side-word span{font-weight:300}
.box-back{padding:26px 16px;display:flex;flex-direction:column;gap:14px}
.box-back .facts h3{font-size:15px}
.box-back .exp{margin-bottom:20px}
</style>
</head>
<body>

<section class="label" aria-label="Bottle wrap label">
  <div class="label-panel label-back">
    <p class="small"><b>Directions:</b> Take one or two capsules after meals. Do not exceed three capsules per day. Take during real-time cravings or before drinking situations for additional craving support. Store in a cool dry place, tightly closed. Keep away from children.</p>
    <p class="small"><b>Directions:</b> Take one or two capsules after meals. Do not exceed three capsules per day. Take during real-time cravings or before drinking situations for additional craving support. Store in a cool dry place, tightly closed. Keep away from children.</p>
    <p class="fda">The FDA has not evaluated these statements. This product is not intended to diagnose, treat, cure, or prevent any disease.</p>
    <div class="base-band"></div>
  </div>
  <div class="label-panel label-front">
    <div class="brand"><span class="brand-dot"></span>Quiet Ridge</div>
    <h1 class="product-name">TOMUVIN</h1>
    <div class="rule"></div>
    <p class="tagline"><strong>Doctor Formulated</strong><br>Developed in Clinical Practice</p>
    <p class="volume">30 ML / 1 FL OZ</p>
    <div class="base-band"></div>
  </div>
  <div class="label-panel label-facts">
    <div class="facts">
      <h3>Supplement Facts</h3>
      <div class="row"><span>Serving Size:</span><span>1 pipette / 20 drops</span></div>
      <div class="row"><span>Servings per Container:</span><span>30</span></div>
      <p class="formula">Active Formula: 280mg (% of Daily Value not Established)</p>
      <p class="ingredients">Pyridoxine, Cobalamin, Folic Acid, Cannabidiol, Aroma Lemon, Aroma Orange, Hemp oil, Lithium Orotate.</p>
    </div>
    <p class="maker">Manufactured in the EU for<br><b>Quiet Ridge, LLC</b><br>Boulder, Colorado, USA<br>Ph. 303-555-0148<br>www.quietridge-care.com<br>EU Distribution by <b>Pelmora Lab. Ltd</b><br>12 Linden Park St., Plovdiv, Bulgaria<br>Ph. 359-555-0192</p>
    <p class="exp">Exp 10.2025</p>
    <div class="base-band"></div>
  </div>
</section>

<section class="box" aria-label="Carton panels">
  <div class="box-panel box-front">
    <div class="brand"><span class="brand-dot"></span>Quiet Ridge</div>
    <h2 class="product-name">TOMUVIN</h2>
    <div class="rule"></div>
    <p class="tagline"><strong>Doctor Formulated</strong><br>Developed in Clinical Practice</p>
    <p class="volume">30 ML / 1 FL OZ</p>
    <div class="base-band"></div>
  </div>
  <div class="box-panel box-side">
    <p class="side-word"><strong>Quiet</strong> <span>Ridge.</span></p>
    <div class="base-band"></div>
  </div>
  <div class="box-panel box-back">
    <div class="facts">
      <h3>Supplement Facts</h3>
      <div class="row"><span>Serving Size:</span><span>1 pipette / 20 drops</span></div>
      <div class="row"><span>Servings per Container:</span><span>30</span></div>
      <p class="formula">Active Formula: 280mg (% of Daily Value not Established)</p>
      <p class="ingredients">Pyridoxine, Cobalamin, Folic Acid, Cannabidiol, Aroma Lemon, Aroma Orange, Hemp oil, Lithium Orotate.</p>
    </div>
    <p class="small"><b>Directions:</b> Take one or two capsules after meals. Do not exceed three capsules per day. Take during real-time cravings or before drinking situations for additional craving support. Store in a cool dry place, tightly closed. Keep away from children.</p>
    <p class="fda">The FDA has not evaluated these statements. This product is not intended to diagnose, treat, cure, or prevent any disease.</p>
    <p class="maker">Manufactured in the EU for<br><b>Quiet Ridge, LLC</b><br>Boulder, Colorado, USA<br>Ph. 303-555-0148<br>www.quietridge-care.com<br>EU Distribution by <b>Pelmora Lab. Ltd</b><br>12 Linden Park St., Plovdiv, Bulgaria<br>Ph. 359-555-0192</p>
    <p class="exp">Exp 10.2025</p>
    <div class="base-band"></div>
  </div>
</section>

</body>
</html>
```